South Carolina Bridal and Formal Wear Store

We want The Gown Parlor of Ashcombe website to feel luxurious, elegant, welcoming, and approachable—without feeling overpriced or intimidating. The site should immediately show that we are a full-service bridal and formal wear destination, offering bridal gowns, prom, mothers’ dresses, tuxedos and suits, accessories, and more. We want beautiful, high-end imagery and a clean, modern design while still reflecting the warm, personal experience customers receive when they walk into our boutique. Most importantly, the website should be easy to shop and navigate, allowing customers to browse our collections, see what we offer, understand price ranges, book appointments, and feel excited and comfortable choosing The Gown Parlor of Ashcombe for all of their special-event needs.

Target Market(s)

Women ages 18-50. Brides, engaged women, mothers of the occasion

Industry/Entity Type

Bridal and Formal Wear

Coding

Coded - Design and coding required

Number of Pages Required

5+ page

Font styles to use
Sans Serif

Colors

Designer to choose colors to be used in the design.

Requirements
Must have
• Appointment area, about us staff area, what we offer and designers our logo
Nice to have
• Modern Southern Luxury: Clean, elegant, and upscale with soft neutral tones, beautiful bridal photography, and a warm Lowcountry feel.
Should not have
• pricing

```html
<!DOCTYPE html>
<html lang="en">
<head>
<meta charset="utf-8">
<title>The Gown Parlor of Ashcombe — Site Pages</title>
<link href="https://fonts.googleapis.com/css2?family=Jost:wght@300;400;500&display=swap" rel="stylesheet">
<style>
:root{
  --dark:#43352f;--cream:#faf7f1;--sand:#efe6da;--gold:#c7a57a;--ink:#3a2e29;
  --muted:#8b7d73;--line:#e4dacd;--card:#fffdf9;--onDark:#d8cdc1;
}
*{box-sizing:border-box;margin:0;padding:0}
html,body{width:1200px;height:1200px;overflow:hidden;background:#fff;font-family:'Jost',sans-serif;color:var(--ink)}
.page{position:absolute;top:28px;width:203px;background:var(--cream);overflow:hidden;box-shadow:0 0 2px rgba(0,0,0,.18)}
.p-home{left:38px}.p-about{left:266px}.p-coll{left:499px}.p-design{left:728px}.p-appt{left:959px}
.sec{position:relative;overflow:hidden;padding:0 19px}
.sand{background:var(--sand)}
.darkbg{background:var(--dark);color:#fff}
.topbar{height:4px;background:#3a2d28;display:flex;justify-content:space-between;align-items:center;padding:0 19px;font-size:1.3px;color:var(--onDark);letter-spacing:.1px}
.navrow{height:10px;background:var(--dark);display:flex;align-items:center;justify-content:space-between;padding:0 19px}
.logo{font-size:2.3px;font-weight:400;color:#fff;letter-spacing:.1px}
.navrow nav{display:flex;gap:2.4px;font-size:1.3px;text-transform:uppercase;color:var(--onDark);margin-left:-30px}
.eb{font-size:1.4px;letter-spacing:.25px;text-transform:uppercase;color:var(--muted)}
.h1{font-size:8.4px;font-weight:300;line-height:1.08;color:#fff}
.h1s{font-size:6px;font-weight:300;line-height:1.15;color:#fff}
.h2{font-size:5.2px;font-weight:300;line-height:1.2;color:var(--ink);margin:1.5px 0 2px}
.h3{font-size:2.4px;font-weight:400;color:var(--ink)}
.tx{font-size:1.7px;line-height:1.6;color:var(--muted)}
.ctr{text-align:center}
.btn{display:inline-block;font-size:1.3px;text-transform:uppercase;letter-spacing:.15px;padding:1.5px 4px;background:var(--dark);color:#fff;white-space:nowrap}
.btn.gold{background:var(--gold);color:#fff}
.btn.ghost{background:none;border:.3px solid var(--line);color:var(--ink)}
.btn.line{background:none;color:#fff;border-bottom:.3px solid #fff;padding:1px 0}
.ph{display:block}
.ph-warm{background:linear-gradient(135deg,#8c7460,#4e3d33 60%,#b19a7f)}
.ph-ivory{background:linear-gradient(135deg,#e8ddcd,#c9b9a3 55%,#f3ede4)}
.ph-sage{background:linear-gradient(135deg,#98a08e,#6c7b63 50%,#c9b6a6)}
.ph-night{background:linear-gradient(135deg,#2c2926,#55504a 55%,#1d1b1a)}
.ph-blush{background:linear-gradient(135deg,#d9c4b4,#a88a78 55%,#efe3d9)}
.ph-street{background:linear-gradient(180deg,#4c4a40,#6f6454 60%,#8b6c55)}
.ph-grey{background:linear-gradient(180deg,#f0eeeb,#9c9893 55%,#817e79)}
.ph-map{background:linear-gradient(135deg,#e6eae0,#d7dfd2 50%,#cfd8e2)}
.hero{position:relative}
.hero .ph{position:absolute;inset:0}
.hero .veil{position:absolute;inset:0;background:linear-gradient(90deg,rgba(40,30,25,.75),rgba(40,30,25,.15))}
.hero .in{position:relative;padding:0 19px}
.card{background:var(--card);border:.3px solid var(--line);padding:2.5px}
.grid4{display:grid;grid-template-columns:repeat(4,1fr);gap:2px}
.grid3{display:grid;grid-template-columns:repeat(3,1fr);gap:2.5px}
.more{font-size:1.3px;text-transform:uppercase;color:var(--muted);margin-top:1.5px}
.avatar{width:6px;height:6px;border-radius:50%;background:var(--gold);margin:0 auto 2px}
.role{font-size:1.2px;text-transform:uppercase;color:var(--gold);letter-spacing:.15px}
.tags{display:flex;flex-wrap:wrap;gap:1px;margin:1.5px 0}
.tag{font-size:1.2px;border:.3px solid var(--line);padding:.6px 1.5px;text-transform:uppercase;color:var(--muted)}
.split{display:flex;gap:6px;align-items:center;height:100%}
.split .ph{width:80px;height:60px;flex:none}
.split .copy{flex:1}
.row{display:flex;justify-content:space-between;align-items:center}
.faq{border-bottom:.3px solid var(--line);padding:2.4px 0;font-size:1.7px;color:var(--ink)}
.foot{background:var(--dark);color:var(--onDark);padding:12px 19px 0;height:81px;position:relative}
.foot .cols{display:grid;grid-template-columns:1.3fr .8fr 1fr 1.4fr;gap:4px}
.foot .logo{font-size:3px;margin-bottom:3px}
.foot h6{font-size:1.3px;text-transform:uppercase;font-weight:400;color:var(--gold);margin-bottom:2px;letter-spacing:.2px}
.foot li{list-style:none;font-size:1.4px;line-height:1.9}
.foot .tx{color:var(--onDark)}
.dots{display:flex;gap:1.5px;margin-top:3px}
.dots span{width:3px;height:3px;border-radius:50%;border:.3px solid var(--onDark)}
.foot .bottom{position:absolute;left:19px;right:19px;bottom:6px;display:flex;justify-content:space-between;font-size:1.2px;border-top:.3px solid #5a4b44;padding-top:2px}
.hrs{display:flex;justify-content:space-between;font-size:1.3px;line-height:1.7}
.dgrid{display:grid;grid-template-columns:repeat(3,1fr);border:.3px solid var(--line)}
.dcell{background:var(--card);border:.3px solid var(--line);padding:2.5px;height:14px}
.dcell b{display:block;font-size:1.9px;font-weight:400;color:var(--ink)}
.dcell i{font-style:normal;font-size:1.2px;text-transform:uppercase;color:var(--muted)}
.dfill{background:#e0d7cb}
.field{margin-bottom:2.4px}
.field label{display:block;font-size:1.2px;color:var(--ink);margin-bottom:.6px}
.field div{height:4px;border:.3px solid var(--line);background:#fff;font-size:1.2px;color:var(--muted);padding:1px 1.2px;overflow:hidden}
.two{display:grid;grid-template-columns:1fr 1fr;gap:3px}
.incl li{list-style:none;font-size:1.3px;line-height:1.75;color:var(--muted)}
.incl li::before{content:"— ";color:var(--gold)}
.dlist{font-size:1.4px;line-height:1.75;color:#e8ddd1;margin-top:1px}
</style>
</head>
<body>

<!-- ============ HOME ============ -->
<main class="page p-home" style="height:1138px">
  <header><div class="topbar"><span>Showroom · Ashcombe · By appointment</span><span>(555) 014-2277 · Email us</span></div>
  <div class="navrow"><span class="logo">The Gown Parlor of Ashcombe</span><nav><span>Home</span><span>About us</span><span>Collections &amp; Services</span><span>Designers</span><span>Appointments</span><span>FAQ</span><span>Contact</span></nav><span class="btn gold">Request an appointment</span></div></header>
  <section class="hero" style="height:73px">
    <span class="ph ph-ivory" role="img" aria-label="Bride in a flowing gown inside a sunlit boutique"></span><div class="veil"></div>
    <div class="in" style="padding-top:6px">
      <p class="eb" style="color:#e9dccb">Welcome to the boutique</p>
      <h1 class="h1" style="margin:1.5px 0 2px">Where the<br>Lowcountry finds<br>the dress</h1>
      <p class="tx" style="color:#eee2d4;width:80px">A full-service bridal and formal wear boutique with a stylist devoted to you and a gown waiting to become yours.</p>
      <p style="margin-top:3px"><span class="btn gold">Request an appointment</span></p>
      <p style="margin-top:3px"><span class="btn line">Explore our collections</span></p>
    </div>
  </section>
  <section class="sec" style="height:99px">
    <div class="split" style="align-items:flex-start;padding-top:14px">
      <div class="copy" style="padding-right:4px">
        <p class="eb">Welcome</p>
        <h2 class="h2">Come as you are. Leave feeling like the bride you imagined.</h2>
        <p class="tx">The Gown Parlor of Ashcombe was built on a simple idea: choosing the dress should feel personal, unhurried and joyful. From the moment you walk in, one consultant guides the whole appointment around you.</p>
        <p class="tx" style="margin-top:2px">We dress brides, bridesmaids, mothers of the occasion, prom guests and groomsmen, with a welcome that is warm and never pressured.</p>
        <p style="margin-top:4px"><span class="btn ghost">Learn more about us</span></p>
      </div>
      <div style="position:relative;width:78px;flex:none;margin-top:6px">
        <span class="ph ph-ivory" style="height:60px" role="img" aria-label="Bright boutique salon with gowns on racks"></span>
        <div class="card" style="position:absolute;left:-3px;bottom:-7px;width:26px;font-size:1.4px;line-height:1.5">One stylist, one bride, one unforgettable appointment</div>
      </div>
    </div>
  </section>
  <section class="sec sand ctr" style="height:131px;padding-top:14px">
    <p class="eb">What we offer</p>
    <h2 class="h2">A full-service boutique for every<br>celebration</h2>
    <p class="tx" style="width:100px;margin:0 auto 8px">Every collection and service we offer, from the first gown fitting to the day your dress is preserved.</p>
    <div class="grid4" style="text-align:left">
      <div class="card" style="height:28px"><p class="h3" style="font-size:1.9px">Bridal</p><p class="tx" style="font-size:1.3px">Curated gowns for every silhouette, styled one-on-one.</p><p class="more">Explore →</p></div>
      <div class="card"><p class="h3" style="font-size:1.9px">Bridesmaids</p><p class="tx" style="font-size:1.3px">Coordinated color stories and flattering cuts for the party.</p><p class="more">Explore →</p></div>
      <div class="card"><p class="h3" style="font-size:1.9px">Mother of the Occasion</p><p class="tx" style="font-size:1.3px">Refined, comfortable gowns for the family.</p><p class="more">Explore →</p></div>
      <div class="card"><p class="h3" style="font-size:1.9px">Tuxedos &amp; Suits</p><p class="tx" style="font-size:1.3px">Rental and purchase options for grooms and guests.</p><p class="more">Explore →</p></div>
      <div class="card" style="height:28px"><p class="h3" style="font-size:1.9px">Formal Wear</p><p class="tx" style="font-size:1.3px">Gowns for galas, military balls and evenings out.</p><p class="more">Explore →</p></div>
      <div class="card"><p class="h3" style="font-size:1.9px">Prom</p><p class="tx" style="font-size:1.3px">A standout prom selection with one-of-a-kind looks.</p><p class="more">Explore →</p></div>
      <div class="card"><p class="h3" style="font-size:1.9px">Wedding Gown Preservation</p><p class="tx" style="font-size:1.3px">Keep your gown safe for years to come.</p><p class="more">Explore →</p></div>
      <div class="card"><p class="h3" style="font-size:1.9px">On-Site Steaming</p><p class="tx" style="font-size:1.3px">Professional steaming before your big day.</p><p class="more">Explore →</p></div>
    </div>
  </section>
  <section class="sec" style="height:137px;padding-top:16px">
    <div style="margin-left:86px"><p class="eb">Pre-appointment experience</p><h2 class="h2">Choose the appointment that fits your day</h2><p class="tx">Walk-ins are always welcome, but an appointment guarantees a consultant.</p></div>
    <div class="split" style="height:auto;align-items:flex-start;margin-top:2px">
      <span class="ph ph-blush" style="width:79px;height:56px" role="img" aria-label="Consultant arranging a veil on a bride"></span>
      <div class="copy">
        <div style="border-bottom:.3px solid var(--line);padding:2px 0"><div class="row"><span class="h3" style="font-size:1.8px">VIP Bridal Appointment</span><span class="eb">2 hours</span></div><p class="tx" style="font-size:1.3px">The entire boutique reserved for your party, with champagne and a dedicated stylist.</p></div>
        <div style="border-bottom:.3px solid var(--line);padding:2px 0"><div class="row"><span class="h3" style="font-size:1.8px">Bridal Appointment</span><span class="eb">1.5 hours</span></div><p class="tx" style="font-size:1.3px">A personalized one-on-one experience with an expert stylist who listens first.</p></div>
        <div style="padding:2px 0"><div class="row"><span class="h3" style="font-size:1.8px">Find My Style Appointment</span><span class="eb">1 hour</span></div><p class="tx" style="font-size:1.3px">For the bride still deciding what she loves; we help narrow the shape.</p></div>
        <p style="margin-top:4px"><span class="btn">Request an appointment</span></p>
      </div>
    </div>
  </section>
  <section class="sec darkbg" style="height:94px;padding-top:16px">
    <p class="eb" style="color:var(--gold)">The designers</p>
    <h2 class="h2" style="color:#fff">Collections we're proud to carry</h2>
    <div class="grid4" style="margin-top:6px">
      <div><p class="eb" style="color:var(--gold)">Bridal</p><p class="dlist">Harlow &amp; Finch<br>Rosalind Hale<br>Corinne Vale<br>Willowmere Bridal Collection</p></div>
      <div><p class="eb" style="color:var(--gold)">Bridesmaids &amp; formal wear</p><p class="dlist">Rosalind Hale<br>Magnolia Row<br>Everett Lane<br>Half Past Seven<br>Sweetgrass Maids</p></div>
      <div><p class="eb" style="color:var(--gold)">Mother of the occasion</p><p class="dlist">Larkspur Eve<br>Bellhaven<br>Everett Lane<br>Half Past Seven</p></div>
      <div><p class="eb" style="color:var(--gold)">Tuxedos &amp; suits</p><p class="dlist">Ridgeway Tailoring<br>Stonebridge Formal</p></div>
    </div>
    <p style="margin-top:8px"><span class="btn gold">Visit our designers</span></p>
  </section>
  <section class="sec ctr" style="height:116px;padding-top:18px">
    <p class="eb">Collections</p>
    <h2 class="h2">Dressed for every seat at the<br>celebration</h2>
    <div class="grid3" style="margin-top:8px;gap:3px">
      <div style="position:relative;height:55px" class="ph ph-sage" role="img" aria-label="Bridesmaids in sage gowns under oak trees"><span class="eb" style="position:absolute;left:2px;bottom:2px;color:#fff">Bridesmaids</span></div>
      <div style="position:relative;height:55px" class="ph ph-night" role="img" aria-label="Tuxedos and suits on a rack"><span class="eb" style="position:absolute;left:2px;bottom:2px;color:#fff">Tuxedos &amp; suits</span></div>
      <div style="position:relative;height:55px" class="ph ph-ivory" role="img" aria-label="Bridal gowns displayed in the salon"><span class="eb" style="position:absolute;left:2px;bottom:2px;color:#fff">Bridal</span></div>
    </div>
  </section>
  <section class="sec sand ctr" style="height:126px;padding-top:14px">
    <p class="eb">Meet the team</p>
    <h2 class="h2">The people who make it feel like<br>home</h2>
    <p class="tx" style="width:100px;margin:0 auto 6px">Our team has walked hundreds of brides down the same happy path, and they will remember your name long after the wedding.</p>
    <div class="grid3">
      <div class="card" style="height:42px;padding-top:5px"><div class="avatar"></div><p class="h3" style="font-size:1.8px">Our Owner</p><p class="role">Owner &amp; lead stylist</p><p class="tx" style="font-size:1.3px">A consultant at heart who opened the boutique to give every bride the experience she deserves.</p></div>
      <div class="card" style="padding-top:5px"><div class="avatar"></div><p class="h3" style="font-size:1.8px">Bridal Consultants</p><p class="role">Styling team</p><p class="tx" style="font-size:1.3px">Our consultants know every gown on the rack by name and listen before they pull a single dress.</p></div>
      <div class="card" style="padding-top:5px"><div class="avatar"></div><p class="h3" style="font-size:1.8px">Formal Wear Specialists</p><p class="role">Grooms, suits &amp; prom</p><p class="tx" style="font-size:1.3px">From groomsmen to prom, every fitting is measured with care and finished on time.</p></div>
    </div>
    <p style="margin-top:6px"><span class="btn ghost">Learn more about us</span></p>
  </section>
  <section class="sec ctr" style="height:96px;padding-top:14px">
    <p class="eb">Good to know</p>
    <h2 class="h2">Questions brides ask us most</h2>
    <div style="width:118px;margin:6px auto 0;text-align:left">
      <div class="faq row"><span>Do I need an appointment?</span><span>+</span></div>
      <div class="faq row"><span>How long do appointments last?</span><span>+</span></div>
      <div class="faq row"><span>What should I bring to my appointment?</span><span>+</span></div>
      <div class="faq row"><span>What sizes are your sample gowns?</span><span>+</span></div>
    </div>
    <p style="margin-top:6px"><span class="btn ghost">View all FAQ</span></p>
  </section>
  <section class="sec" style="height:102px;padding:0">
    <div style="display:flex;height:100%">
      <div style="width:102px;padding:16px 8px 0 8px">
        <p class="eb">Visit us</p>
        <h2 class="h2">418 Harbor Lane, Ashcombe</h2>
        <p class="tx" style="margin-top:4px">⌖ 418 Harbor Lane, Suite 100, Ashcombe</p>
        <p class="tx">☏ (555) 014-2277</p>
        <p class="tx">✉ appointments@gownparlorashcombe.com</p>
        <div style="width:60px;margin-top:2px">
          <div class="hrs"><span>Sunday</span><span>Closed</span></div><div class="hrs"><span>Monday</span><span>Closed</span></div><div class="hrs"><span>Tuesday</span><span>Closed</span></div><div class="hrs"><span>Wednesday</span><span>10:00 AM – 6:00 PM</span></div><div class="hrs"><span>Thursday</span><span>10:00 AM – 6:00 PM</span></div><div class="hrs"><span>Friday</span><span>10:00 AM – 6:00 PM</span></div><div class="hrs"><span>Saturday</span><span>10:00 AM – 4:00 PM</span></div>
        </div>
        <p style="margin-top:3px"><span class="btn">Request an appointment</span> <span class="btn ghost">Contact us</span></p>
      </div>
      <div style="flex:1;display:flex;flex-direction:column"><div style="height:40px;background:#e6e4e0"></div><span class="ph ph-map" style="flex:1" role="img" aria-label="Map showing the boutique location"></span></div>
    </div>
  </section>
  <section class="hero ctr" style="height:67px">
    <span class="ph ph-grey" role="img" aria-label="Soft gown fabric in a bright room"></span>
    <div class="in" style="padding-top:20px">
      <p class="h1s" style="font-size:4px;margin:0 auto 3px;width:110px">Life's most special occasions deserve a boutique that treats them that way</p>
      <span class="btn gold">Request an appointment</span>
    </div>
  </section>
  <footer class="foot">
    <div class="cols">
      <div><p class="logo">The Gown Parlor of Ashcombe</p><p class="tx" style="font-size:1.3px">A full-service bridal and formal wear boutique in the heart of the Lowcountry, where every celebration is treated like our own.</p><div class="dots"><span></span><span></span></div></div>
      <div><h6>Explore</h6><ul><li>Home</li><li>About Us</li><li>Collections &amp; Services</li><li>Designers</li><li>Appointments</li><li>FAQ</li><li>Contact</li></ul></div>
      <div><h6>What we offer</h6><ul><li>Bridal</li><li>Bridesmaids</li><li>Mother of the Occasion</li><li>Tuxedos &amp; Suits</li><li>Formal Wear</li><li>Prom</li><li>Wedding Gown Preservation</li><li>On-Site Steaming</li></ul></div>
      <div><h6>Visit us</h6><p class="tx" style="font-size:1.3px">418 Harbor Lane, Suite 100<br>Ashcombe<br>(555) 014-2277<br>appointments@gownparlorashcombe.com</p><div class="hrs"><span>Wed – Fri</span><span>10:00 AM – 6:00 PM</span></div><div class="hrs"><span>Saturday</span><span>10:00 AM – 4:00 PM</span></div><p style="margin-top:3px"><span class="btn gold">Request an appointment</span></p></div>
    </div>
    <div class="bottom"><span>© 2025 The Gown Parlor of Ashcombe. All rights reserved.</span><span>Ashcombe · Walk-ins welcome · Appointments preferred</span></div>
  </footer>
</main>

<!-- ============ ABOUT ============ -->
<main class="page p-about" style="height:510px">
  <header><div class="topbar"><span>Showroom · Ashcombe · By appointment</span><span>(555) 014-2277 · Email us</span></div>
  <div class="navrow"><span class="logo">The Gown Parlor of Ashcombe</span><nav><span>Home</span><span>About us</span><span>Collections &amp; Services</span><span>Designers</span><span>Appointments</span><span>FAQ</span><span>Contact</span></nav><span class="btn gold">Request an appointment</span></div></header>
  <section class="hero" style="height:50px">
    <span class="ph ph-warm" role="img" aria-label="Boutique interior with gowns and floral arrangements"></span><div class="veil"></div>
    <div class="in" style="padding-top:14px"><p class="eb" style="color:#e9dccb">About us</p><h1 class="h1s">A boutique built on Southern<br>hospitality</h1><p class="tx" style="color:#eee2d4;width:80px">A family-owned bridal and formal wear boutique with a personal welcome.</p></div>
  </section>
  <section class="sec" style="height:106px;padding-top:16px">
    <div class="split" style="align-items:flex-start">
      <div class="copy"><p class="eb">Our story</p><h2 class="h2" style="font-size:4.6px">Ashcombe's full-service bridal destination</h2>
        <p class="tx">The Gown Parlor of Ashcombe began with a belief that shopping for the most important dress of your life should feel like visiting a friend's home: relaxed, personal and full of joy.</p>
        <p class="tx" style="margin-top:2px">Today we are a full-service boutique dressing brides, bridesmaids, mothers of the occasion, prom guests and groomsmen. Our consultants know every gown by heart.</p>
        <p class="tx" style="margin-top:2px">And when the celebration is over, we are still here, cleaning and preserving your gown as an authorized partner of a trusted preservation studio.</p></div>
      <span class="ph ph-blush" style="width:79px;height:57px;margin-top:8px" role="img" aria-label="Consultant fitting a veil on a bride"></span>
    </div>
  </section>
  <section class="sec sand ctr" style="height:78px;padding-top:14px">
    <p class="eb">What we believe</p><h2 class="h2">Luxury, without a hint of intimidation</h2>
    <div class="grid4" style="text-align:left;margin-top:6px">
      <div class="card" style="height:22px"><p class="h3" style="font-size:1.7px">Southern Hospitality</p><p class="tx" style="font-size:1.3px">Sweet tea, warm greetings and a relaxed pace from the moment you arrive.</p></div>
      <div class="card"><p class="h3" style="font-size:1.7px">Personal Attention</p><p class="tx" style="font-size:1.3px">One consultant stays with you through every gown you try.</p></div>
      <div class="card"><p class="h3" style="font-size:1.7px">Curated, Not Crowded</p><p class="tx" style="font-size:1.3px">Every gown on our floor is chosen by hand, never by volume.</p></div>
      <div class="card"><p class="h3" style="font-size:1.7px">Honest Guidance</p><p class="tx" style="font-size:1.3px">We listen to your budget and tell you what truly flatters you.</p></div>
    </div>
  </section>
  <section class="sec ctr" style="height:117px;padding-top:16px">
    <p class="eb">Meet the team</p><h2 class="h2">The faces you'll see when you walk in</h2>
    <p class="tx" style="width:100px;margin:0 auto 6px">Our consultants are the reason brides come back with their sisters, their friends and eventually their daughters.</p>
    <div class="grid3" style="text-align:left">
      <div class="card" style="height:42px;padding-top:4px"><div class="avatar" style="margin-left:0"></div><p class="h3" style="font-size:1.8px">Our Owner</p><p class="role">Owner &amp; lead stylist</p><p class="tx" style="font-size:1.3px">A consultant at heart who opened the doors to give every bride a calm, joyful visit.</p></div>
      <div class="card" style="padding-top:4px"><div class="avatar" style="margin-left:0"></div><p class="h3" style="font-size:1.8px">Bridal Consultants</p><p class="role">Styling team</p><p class="tx" style="font-size:1.3px">Our consultants know every gown on the rack and pull with care.</p></div>
      <div class="card" style="padding-top:4px"><div class="avatar" style="margin-left:0"></div><p class="h3" style="font-size:1.8px">Formal Wear Specialists</p><p class="role">Grooms, suits &amp; prom</p><p class="tx" style="font-size:1.3px">From groomsmen to prom, fittings are measured and finished on time.</p></div>
    </div>
    <p class="tx" style="text-align:left;margin-top:4px;font-size:1.3px">Individual team introductions and portraits will be added here shortly.</p>
  </section>
  <section class="hero ctr" style="height:50px">
    <span class="ph ph-street" role="img" aria-label="Historic Lowcountry street lined with palms and oaks"></span><div class="veil" style="background:rgba(40,30,25,.35)"></div>
    <div class="in" style="padding-top:17px"><p class="h1s" style="font-size:4.4px;margin-bottom:3px">We'd love to meet you in person</p><span class="btn gold">Request an appointment</span></div>
  </section>
  <div style="height:14px"></div>
  <footer class="foot">
    <div class="cols">
      <div><p class="logo">The Gown Parlor of Ashcombe</p><p class="tx" style="font-size:1.3px">A full-service bridal and formal wear boutique in the heart of the Lowcountry, where every celebration is treated like our own.</p><div class="dots"><span></span><span></span></div></div>
      <div><h6>Explore</h6><ul><li>Home</li><li>About Us</li><li>Collections &amp; Services</li><li>Designers</li><li>Appointments</li><li>FAQ</li><li>Contact</li></ul></div>
      <div><h6>What we offer</h6><ul><li>Bridal</li><li>Bridesmaids</li><li>Mother of the Occasion</li><li>Tuxedos &amp; Suits</li><li>Formal Wear</li><li>Prom</li><li>Wedding Gown Preservation</li><li>On-Site Steaming</li></ul></div>
      <div><h6>Visit us</h6><p class="tx" style="font-size:1.3px">418 Harbor Lane, Suite 100<br>Ashcombe<br>(555) 014-2277<br>appointments@gownparlorashcombe.com</p><div class="hrs"><span>Wed – Fri</span><span>10:00 AM – 6:00 PM</span></div><div class="hrs"><span>Saturday</span><span>10:00 AM – 4:00 PM</span></div><p style="margin-top:3px"><span class="btn gold">Request an appointment</span></p></div>
    </div>
    <div class="bottom"><span>© 2025 The Gown Parlor of Ashcombe. All rights reserved.</span><span>Ashcombe · Walk-ins welcome · Appointments preferred</span></div>
  </footer>
</main>

<!-- ============ COLLECTIONS ============ -->
<main class="page p-coll" style="height:927px">
  <header><div class="topbar"><span>Showroom · Ashcombe · By appointment</span><span>(555) 014-2277 · Email us</span></div>
  <div class="navrow"><span class="logo">The Gown Parlor of Ashcombe</span><nav><span>Home</span><span>About us</span><span>Collections &amp; Services</span><span>Designers</span><span>Appointments</span><span>FAQ</span><span>Contact</span></nav><span class="btn gold">Request an appointment</span></div></header>
  <section class="hero" style="height:50px">
    <span class="ph ph-sage" role="img" aria-label="Bridal party in sage gowns"></span><div class="veil"></div>
    <div class="in" style="padding-top:20px"><p class="eb" style="color:#e9dccb">Collections &amp; services</p><h1 class="h1s">Everything under one roof</h1><p class="tx" style="color:#eee2d4;width:80px">Bridal, party, formal and aftercare in one welcoming boutique.</p></div>
  </section>
  <div class="sec" style="height:6px;display:flex;gap:3px;align-items:center;font-size:1.2px;text-transform:uppercase;color:var(--muted);border-bottom:.3px solid var(--line)"><span>Bridal</span><span>Bridesmaids</span><span>Mother of the occasion</span><span>Tuxedos &amp; suits</span><span>Formal wear</span><span>Prom</span><span>Gown preservation</span><span>On-site steaming</span></div>

  <section class="sec" style="height:99px"><div class="split">
    <span class="ph ph-ivory" role="img" aria-label="Bride in a fitted white gown"></span>
    <div class="copy"><p class="eb">01</p><h2 class="h2">Bridal</h2><p class="tx">Curated gowns for every silhouette, styled one-on-one with a consultant who listens.</p><p class="tx">Our bridal salon is open by appointment, with lace, crepe and satin designs in a wide range of sizes.</p><p class="eb" style="margin-top:2px">Designers</p><div class="tags"><span class="tag">Harlow &amp; Finch</span><span class="tag">Rosalind Hale</span><span class="tag">Corinne Vale</span><span class="tag">Willowmere Bridal</span></div><span class="btn">Request an appointment</span> <span class="btn ghost">Visit our designers</span></div>
  </div></section>
  <section class="sec" style="height:89px"><div class="split">
    <div class="copy"><p class="eb">02</p><h2 class="h2">Bridesmaids</h2><p class="tx">Coordinated color stories and flattering cuts for your whole party, in every size.</p><p class="tx">We help you build a palette, mix styles and manage orders so everyone arrives ready.</p><p class="eb" style="margin-top:2px">Designers</p><div class="tags"><span class="tag">Rosalind Hale</span><span class="tag">Magnolia Row</span><span class="tag">Everett Lane</span><span class="tag">Half Past Seven</span><span class="tag">Sweetgrass Maids</span></div><span class="btn">Request an appointment</span> <span class="btn ghost">Visit our designers</span></div>
    <span class="ph ph-sage" role="img" aria-label="Bridesmaids in sage and blush gowns outdoors"></span>
  </div></section>
  <section class="sec" style="height:91px"><div class="split">
    <span class="ph ph-blush" role="img" aria-label="Champagne gowns for mothers of the occasion"></span>
    <div class="copy"><p class="eb">03</p><h2 class="h2">Mother of the Occasion</h2><p class="tx">Refined, comfortable gowns for the mothers and grandmothers of the celebration.</p><p class="tx">Elegant beading, sleeve options and soft jewel tones chosen to complement the party.</p><p class="eb" style="margin-top:2px">Designers</p><div class="tags"><span class="tag">Larkspur Eve</span><span class="tag">Bellhaven</span><span class="tag">Everett Lane</span><span class="tag">Half Past Seven</span></div><span class="btn">Request an appointment</span> <span class="btn ghost">Visit our designers</span></div>
  </div></section>
  <section class="sec" style="height:92px"><div class="split">
    <div class="copy"><p class="eb">04</p><h2 class="h2">Tuxedos &amp; Suits</h2><p class="tx">Rental and purchase options for the groom, groomsmen and every guest of honor.</p><p class="tx">Book a fitting, pick a style and we handle measurements for the whole party.</p><p class="eb" style="margin-top:2px">Designers</p><div class="tags"><span class="tag">Ridgeway Tailoring</span><span class="tag">Stonebridge Formal</span></div><span class="btn">Request an appointment</span> <span class="btn ghost">Visit our designers</span></div>
    <span class="ph ph-night" role="img" aria-label="Tuxedo jackets and bow ties"></span>
  </div></section>
  <section class="sec" style="height:91px"><div class="split">
    <span class="ph ph-blush" role="img" aria-label="Evening gowns on a rack"></span>
    <div class="copy"><p class="eb">05</p><h2 class="h2">Formal Wear</h2><p class="tx">Polished gowns for galas, military balls, pageants and every evening event.</p><p class="tx">From timeless black to bold color, our formal collection is chosen for a perfect entrance.</p><p class="eb" style="margin-top:2px">Designers</p><div class="tags"><span class="tag">Rosalind Hale</span><span class="tag">Magnolia Row</span><span class="tag">Everett Lane</span><span class="tag">Half Past Seven</span></div><span class="btn">Request an appointment</span> <span class="btn ghost">Visit our designers</span></div>
  </div></section>
  <section class="sec" style="height:85px"><div class="split">
    <div class="copy"><p class="eb">06</p><h2 class="h2">Prom</h2><p class="tx">A standout prom selection with one-of-a-kind looks registered by school.</p><p class="tx">Request a Prom Gown Appointment and bring your friends for a fun fitting.</p><p style="margin-top:3px"><span class="btn">Request an appointment</span></p></div>
    <span class="ph ph-sage" role="img" aria-label="Group of young women in gowns outdoors"></span>
  </div></section>
  <section class="sec" style="height:88px"><div class="split">
    <span class="ph ph-ivory" role="img" aria-label="Sunlit salon with gowns and a mirror"></span>
    <div class="copy"><p class="eb">07</p><h2 class="h2">Wedding Gown Preservation</h2><p class="tx">An authorized partner of a trusted preservation studio. Your gown is cleaned, boxed and protected for the years to come, ready for the daughters who follow.</p><p style="margin-top:3px"><span class="btn">Request an appointment</span></p></div>
  </div></section>
  <section class="sec" style="height:85px"><div class="split">
    <div class="copy"><p class="eb">08</p><h2 class="h2">On-Site Steaming</h2><p class="tx">Professional steaming in the boutique before your big day. Bring your gown or formal wear to us and we will have it pressed and ready.</p><p style="margin-top:3px"><span class="btn">Request an appointment</span></p></div>
    <span class="ph ph-blush" role="img" aria-label="Consultant steaming a veil"></span>
  </div></section>
  <section class="sec sand ctr" style="height:43px;padding-top:8px">
    <h2 class="h2" style="font-size:4px">Not sure where to start?</h2><p class="tx" style="width:100px;margin:0 auto 3px">Tell us about your event and we'll match you with the right appointment and consultant.</p><span class="btn">Request an appointment</span>
  </section>
  <div style="height:12px"></div>
  <footer class="foot">
    <div class="cols">
      <div><p class="logo">The Gown Parlor of Ashcombe</p><p class="tx" style="font-size:1.3px">A full-service bridal and formal wear boutique in the heart of the Lowcountry, where every celebration is treated like our own.</p><div class="dots"><span></span><span></span></div></div>
      <div><h6>Explore</h6><ul><li>Home</li><li>About Us</li><li>Collections &amp; Services</li><li>Designers</li><li>Appointments</li><li>FAQ</li><li>Contact</li></ul></div>
      <div><h6>What we offer</h6><ul><li>Bridal</li><li>Bridesmaids</li><li>Mother of the Occasion</li><li>Tuxedos &amp; Suits</li><li>Formal Wear</li><li>Prom</li><li>Wedding Gown Preservation</li><li>On-Site Steaming</li></ul></div>
      <div><h6>Visit us</h6><p class="tx" style="font-size:1.3px">418 Harbor Lane, Suite 100<br>Ashcombe<br>(555) 014-2277<br>appointments@gownparlorashcombe.com</p><div class="hrs"><span>Wed – Fri</span><span>10:00 AM – 6:00 PM</span></div><div class="hrs"><span>Saturday</span><span>10:00 AM – 4:00 PM</span></div><p style="margin-top:3px"><span class="btn gold">Request an appointment</span></p></div>
    </div>
    <div class="bottom"><span>© 2025 The Gown Parlor of Ashcombe. All rights reserved.</span><span>Ashcombe · Walk-ins welcome · Appointments preferred</span></div>
  </footer>
</main>

<!-- ============ DESIGNERS ============ -->
<main class="page p-design" style="height:497px">
  <header><div class="topbar"><span>Showroom · Ashcombe · By appointment</span><span>(555) 014-2277 · Email us</span></div>
  <div class="navrow"><span class="logo">The Gown Parlor of Ashcombe</span><nav><span>Home</span><span>About us</span><span>Collections &amp; Services</span><span>Designers</span><span>Appointments</span><span>FAQ</span><span>Contact</span></nav><span class="btn gold">Request an appointment</span></div></header>
  <section class="hero" style="height:50px">
    <span class="ph ph-blush" role="img" aria-label="Smiling bridal party in neutral gowns"></span><div class="veil"></div>
    <div class="in" style="padding-top:14px"><p class="eb" style="color:#e9dccb">Our designers</p><h1 class="h1s">Collections chosen with<br>intention</h1><p class="tx" style="color:#eee2d4;width:80px">Every label we carry is chosen for fit, quality and value.</p></div>
  </section>
  <section class="sec" style="height:82px;padding-top:14px">
    <p class="eb">Bridal</p><h2 class="h2" style="font-size:4.4px">Gowns for the bride, from timeless to<br>modern.</h2>
    <div class="dgrid" style="margin-top:5px">
      <div class="dcell"><b>Harlow &amp; Finch</b><i>Visit designer site ↗</i></div><div class="dcell"><b>Rosalind Hale</b><i>Visit designer site ↗</i></div><div class="dcell"><b>Corinne Vale</b><i>Visit designer site ↗</i></div>
      <div class="dcell"><b>Willowmere Bridal Collection</b><i>Available in-boutique</i></div><div class="dcell dfill" style="grid-column:span 2"></div>
    </div>
  </section>
  <section class="sec" style="height:75px;padding-top:6px">
    <p class="eb">Bridesmaids &amp; formal wear</p><h2 class="h2" style="font-size:4.4px">Color-rich collections for the whole<br>party.</h2>
    <div class="dgrid" style="margin-top:5px">
      <div class="dcell"><b>Rosalind Hale</b><i>Visit designer site ↗</i></div><div class="dcell"><b>Magnolia Row</b><i>Visit designer site ↗</i></div><div class="dcell"><b>Everett Lane</b><i>Visit designer site ↗</i></div>
      <div class="dcell"><b>Half Past Seven</b><i>Visit designer site ↗</i></div><div class="dcell"><b>Sweetgrass Maids</b><i>Visit designer site ↗</i></div><div class="dcell dfill"></div>
    </div>
  </section>
  <section class="sec" style="height:75px;padding-top:6px">
    <p class="eb">Mother of the occasion</p><h2 class="h2" style="font-size:4.4px">Sophisticated gowns for mothers and<br>grandmothers.</h2>
    <div class="dgrid" style="margin-top:5px">
      <div class="dcell"><b>Larkspur Eve</b><i>Visit designer site ↗</i></div><div class="dcell"><b>Bellhaven</b><i>Visit designer site ↗</i></div><div class="dcell"><b>Everett Lane</b><i>Visit designer site ↗</i></div>
      <div class="dcell"><b>Half Past Seven</b><i>Visit designer site ↗</i></div><div class="dcell dfill" style="grid-column:span 2"></div>
    </div>
  </section>
  <section class="sec" style="height:57px;padding-top:6px">
    <p class="eb">Tuxedos &amp; formal wear</p><h2 class="h2" style="font-size:4.4px">Rental and purchase programs for the<br>gentlemen.</h2>
    <div class="dgrid" style="margin-top:5px">
      <div class="dcell"><b>Ridgeway Tailoring</b><i>Visit designer site ↗</i></div><div class="dcell"><b>Stonebridge Formal</b><i>Visit designer site ↗</i></div><div class="dcell dfill"></div>
    </div>
  </section>
  <section class="sec sand ctr" style="height:50px;padding-top:10px">
    <h2 class="h2" style="font-size:4px">See these collections in person</h2><p class="tx" style="width:100px;margin:0 auto 3px">Designer availability varies by season. Request an appointment and we'll pull the collections that suit your style.</p>
    <span class="btn">Request an appointment</span> <span class="btn ghost">Collections &amp; services</span>
  </section>
  <div style="height:13px"></div>
  <footer class="foot">
    <div class="cols">
      <div><p class="logo">The Gown Parlor of Ashcombe</p><p class="tx" style="font-size:1.3px">A full-service bridal and formal wear boutique in the heart of the Lowcountry, where every celebration is treated like our own.</p><div class="dots"><span></span><span></span></div></div>
      <div><h6>Explore</h6><ul><li>Home</li><li>About Us</li><li>Collections &amp; Services</li><li>Designers</li><li>Appointments</li><li>FAQ</li><li>Contact</li></ul></div>
      <div><h6>What we offer</h6><ul><li>Bridal</li><li>Bridesmaids</li><li>Mother of the Occasion</li><li>Tuxedos &amp; Suits</li><li>Formal Wear</li><li>Prom</li><li>Wedding Gown Preservation</li><li>On-Site Steaming</li></ul></div>
      <div><h6>Visit us</h6><p class="tx" style="font-size:1.3px">418 Harbor Lane, Suite 100<br>Ashcombe<br>(555) 014-2277<br>appointments@gownparlorashcombe.com</p><div class="hrs"><span>Wed – Fri</span><span>10:00 AM – 6:00 PM</span></div><div class="hrs"><span>Saturday</span><span>10:00 AM – 4:00 PM</span></div><p style="margin-top:3px"><span class="btn gold">Request an appointment</span></p></div>
    </div>
    <div class="bottom"><span>© 2025 The Gown Parlor of Ashcombe. All rights reserved.</span><span>Ashcombe · Walk-ins welcome · Appointments preferred</span></div>
  </footer>
</main>

<!-- ============ APPOINTMENTS ============ -->
<main class="page p-appt" style="height:557px">
  <header><div class="topbar"><span>Showroom · Ashcombe · By appointment</span><span>(555) 014-2277 · Email us</span></div>
  <div class="navrow"><span class="logo">The Gown Parlor of Ashcombe</span><nav><span>Home</span><span>About us</span><span>Collections &amp; Services</span><span>Designers</span><span>Appointments</span><span>FAQ</span><span>Contact</span></nav><span class="btn gold">Request an appointment</span></div></header>
  <section class="hero" style="height:50px">
    <span class="ph ph-warm" role="img" aria-label="Consultant preparing a bride in the salon"></span><div class="veil"></div>
    <div class="in" style="padding-top:18px"><p class="eb" style="color:#e9dccb">Appointments</p><h1 class="h1s">Reserve your time with us</h1><p class="tx" style="color:#eee2d4;width:80px">Walk-ins are welcome, but an appointment holds a consultant just for you.</p></div>
  </section>
  <section class="sec" style="height:143px;padding:20px 19px 0 25px">
    <div style="display:flex;gap:7px">
      <div style="width:81px">
        <p class="eb">Request an appointment</p><h2 class="h2" style="font-size:4px">Tell us about your visit</h2>
        <div class="field" style="margin-top:4px"><label>Appointment type *</label><div>Select an appointment type</div></div>
        <div class="two"><div class="field"><label>Preferred day *</label><div>mm/dd/yyyy</div></div><div class="field"><label>Preferred time *</label><div>Select a time</div></div></div>
        <div class="field"><label>Full name *</label><div>Your name</div></div>
        <div class="two"><div class="field"><label>Email *</label><div>you@example.com</div></div><div class="field"><label>Phone *</label><div>(555) 000-0000</div></div></div>
        <div class="field"><label>Notes or questions</label><div style="height:12px">Wedding date, guest count, styles you love, anything we should know</div></div>
        <div class="btn" style="display:block;text-align:center">Submit appointment request</div>
        <p class="tx" style="font-size:1.2px;margin-top:2px">Requests are confirmed by phone or email within one business day.</p>
      </div>
      <aside style="flex:1;background:var(--sand);padding:3px;height:76px">
        <p class="eb">Before you visit</p><h3 class="h3" style="font-size:2.4px;font-weight:300;margin:1px 0 2px">Walk-ins welcome, appointments recommended</h3>
        <p class="tx" style="font-size:1.3px">When you book ahead, a consultant reserves time and pulls gowns in your style before you arrive.</p>
        <p class="tx" style="font-size:1.3px;margin-top:1.5px">Need a time outside our normal hours? Call or email us and we will do our best to make it work.</p>
        <ul class="incl" style="margin-top:1.5px"><li>Bring a shoe in a similar heel height</li><li>Wear nude undergarments</li><li>Limit your guests to your closest few</li><li>Arrive five minutes early</li></ul>
      </aside>
    </div>
  </section>
  <section class="sec sand" style="height:283px;padding-top:10px">
    <div class="ctr"><p class="eb">Appointment types</p><h2 class="h2">Choose the experience that suits you</h2></div>
    <div class="card" style="margin-top:6px;height:64px;display:flex;gap:4px">
      <div style="flex:1.2"><span class="btn gold" style="font-size:1.1px;padding:.8px 2px">Most exclusive</span><p class="h3" style="margin-top:1.5px">VIP Bridal Appointment</p><p class="role">2 hours · private boutique</p><p class="tx" style="font-size:1.3px;margin-top:1px">The entire boutique reserved for you and your guests, with champagne, a dedicated consultant and a full look styled from veil to shoe.</p><p class="tx" style="font-size:1.3px;margin-top:1px">A booking deposit is required and applied toward your gown purchase. Cancellations need 48 hours' notice.</p></div>
      <div style="flex:1"><p class="eb">Included</p><ul class="incl"><li>Entire boutique reserved for your party</li><li>Two dedicated bridal consultants</li><li>Champagne and light bites</li><li>Gowns pulled before you arrive</li><li>Accessory styling session</li><li>Personalized thank-you gift</li></ul><p class="eb" style="margin-top:2px">Bring with you</p><div class="tags"><span class="tag">Shoes</span><span class="tag">Inspiration photos</span><span class="tag">Up to six guests</span></div></div>
    </div>
    <div class="card" style="margin-top:4px;height:48px;display:flex;gap:4px">
      <div style="flex:1.2"><p class="h3">Bridal Appointment</p><p class="role">1.5 hours · one-on-one</p><p class="tx" style="font-size:1.3px;margin-top:1px">A personalized one-on-one experience with an expert stylist who listens to your vision and walks you through the collection.</p><p class="tx" style="font-size:1.3px;margin-top:1px">A small booking fee is applied toward your gown purchase.</p></div>
      <div style="flex:1"><p class="eb">Included</p><ul class="incl"><li>Dedicated bridal consultant</li><li>Curated gown selection</li><li>Veil and accessory styling</li><li>Up to four guests</li></ul></div>
    </div>
    <div class="card" style="margin-top:4px;height:44px;display:flex;gap:4px">
      <div style="flex:1.2"><p class="h3">Find My Style Appointment</p><p class="role">1 hour · exploration</p><p class="tx" style="font-size:1.3px;margin-top:1px">For the bride still deciding what she loves. We try a little of everything and help you narrow your shape before a full visit.</p></div>
      <div style="flex:1"><p class="eb">Included</p><ul class="incl"><li>Relaxed styling session</li><li>Silhouette guidance</li><li>Notes for your next visit</li></ul></div>
    </div>
    <div style="display:grid;grid-template-columns:repeat(5,1fr);gap:2px;margin-top:4px">
      <div class="card" style="height:34px"><p class="h3" style="font-size:1.6px">Bridesmaid Appointment</p><p class="role">1 hour</p><p class="tx" style="font-size:1.2px">Bring the party to shop colors and styles together.</p></div>
      <div class="card"><p class="h3" style="font-size:1.6px">Mother of the Occasion Appointment</p><p class="role">1 hour</p><p class="tx" style="font-size:1.2px">Elegant options chosen for comfort and style.</p></div>
      <div class="card"><p class="h3" style="font-size:1.6px">Tuxedo / Suit Appointment</p><p class="role">30 minutes</p><p class="tx" style="font-size:1.2px">Select styles, complete fittings and measurements.</p></div>
      <div class="card"><p class="h3" style="font-size:1.6px">Formal Wear Appointment</p><p class="role">1 hour</p><p class="tx" style="font-size:1.2px">For galas, balls and every evening event.</p></div>
      <div class="card"><p class="h3" style="font-size:1.6px">Prom Gown Appointment</p><p class="role">1 hour</p><p class="tx" style="font-size:1.2px">A relaxed fitting to find the gown of the night.</p></div>
    </div>
  </section>
  <footer class="foot">
    <div class="cols">
      <div><p class="logo">The Gown Parlor of Ashcombe</p><p class="tx" style="font-size:1.3px">A full-service bridal and formal wear boutique in the heart of the Lowcountry, where every celebration is treated like our own.</p><div class="dots"><span></span><span></span></div></div>
      <div><h6>Explore</h6><ul><li>Home</li><li>About Us</li><li>Collections &amp; Services</li><li>Designers</li><li>Appointments</li><li>FAQ</li><li>Contact</li></ul></div>
      <div><h6>What we offer</h6><ul><li>Bridal</li><li>Bridesmaids</li><li>Mother of the Occasion</li><li>Tuxedos &amp; Suits</li><li>Formal Wear</li><li>Prom</li><li>Wedding Gown Preservation</li><li>On-Site Steaming</li></ul></div>
      <div><h6>Visit us</h6><p class="tx" style="font-size:1.3px">418 Harbor Lane, Suite 100<br>Ashcombe<br>(555) 014-2277<br>appointments@gownparlorashcombe.com</p><div class="hrs"><span>Wed – Fri</span><span>10:00 AM – 6:00 PM</span></div><div class="hrs"><span>Saturday</span><span>10:00 AM – 4:00 PM</span></div><p style="margin-top:3px"><span class="btn gold">Request an appointment</span></p></div>
    </div>
    <div class="bottom"><span>© 2025 The Gown Parlor of Ashcombe. All rights reserved.</span><span>Ashcombe · Walk-ins welcome · Appointments preferred</span></div>
  </footer>
</main>

</body>
</html>
```